Aerospace & Defense Manufacturing Firm

Brochure for a contract manufacturing service provider in precision sheet metal, precision machining, complicated assemblies, and welding. We specialize in fast turnaround support in Military, Defense, Aerospace, High Technology and Automotive sectors.

Target Market(s)

Manufacturing OEMs

Font styles to use
Sans Serif

Requirements
Must have
• S standout brocure with specifics about what we do
Nice to have
• Looking for a standard or tri-fold brochure with catches the eye of our target audience, corporate procurement agents.
Should not have
• Anything that is informal or trendy. The target audience is large multi-national corproations, so anything "locally cool or hype" might not be appropriate.

```html
<!DOCTYPE html>
<html lang="en">
<head>
<meta charset="utf-8">
<title>Vantor Industrial Manufacturing – What we do</title>
<link rel="stylesheet" href="https://fonts.googleapis.com/css2?family=Roboto:wght@300;400;500;700;900&display=swap">
<style>
  :root{
    --sky:#66c4de;
    --navy:#061733;
    --navy-deep:#0a1628;
    --panel:#c9ebf3;
    --tile:#e8f5f9;
    --ink:#0d1a33;
    --white:#ffffff;
    --part-grey:#a9adb1;
    --part-light:#d9dcde;
    --part-beige:#d6d2b8;
    --part-dark:#2c3034;
    --part-yellow:#e8b81c;
  }
  *{box-sizing:border-box;margin:0;padding:0}
  html,body{width:1200px;height:849px;overflow:hidden;background:var(--white)}
  body{font-family:"Roboto",Arial,sans-serif;color:var(--ink);position:relative}
  .abs{position:absolute}

  .intro-head{left:0;top:0;width:392px;height:115px;background:var(--white)}
  .accent-bar{position:absolute;width:4px;background:var(--sky)}
  .page-title{position:absolute;left:73px;top:38px;font-weight:300;font-size:40px;letter-spacing:-1.5px;color:var(--ink);line-height:1}

  .intro-panel{left:0;top:116px;width:392px;height:300px;background:var(--panel);padding:18px 0 0 43px}
  .intro-panel p{font-weight:300;font-size:15.4px;line-height:18.85px;color:#1d2a3f;white-space:nowrap}

  .sector-head{top:0;height:108px;padding:46px 0 0 25px;color:var(--white);font-weight:700;font-size:19px;line-height:23.5px;letter-spacing:.2px}
  .sector-head.sky{background:var(--sky)}
  .sector-head.navy{background:var(--navy)}
  .sector-desc{top:116px;height:131px;background:var(--tile);padding:14px 0 0 20px;font-size:13.8px;line-height:16.5px;color:#14203a;white-space:nowrap}
  .sector-photo{top:257px;height:158px}

  .services{left:0;top:423px;width:392px;height:426px;
    background:repeating-linear-gradient(90deg,#0b2445 0,#0e2d52 2px,#0a2140 4px,#0c2849 7px);}
  .services-title{position:absolute;left:75px;top:32px;font-weight:300;font-size:38px;line-height:35px;letter-spacing:-1px;color:var(--white)}
  .service{position:absolute;left:0;width:380px;background:var(--navy-deep);display:flex;align-items:center;padding-left:43px;
    color:var(--white);font-weight:700;font-size:17.5px;line-height:22px}
  .service::before{content:"";position:absolute;left:0;top:0;bottom:0;width:19px;
    background:linear-gradient(180deg,#777 0%,#f4f4f4 35%,#9a9a9a 60%,#eee 85%,#666 100%)}
  .steel-strip{position:absolute;left:0;bottom:0;width:392px;height:22px;
    background:linear-gradient(90deg,#5a5e63 0%,#d8dadc 30%,#8e9297 55%,#eceeef 75%,#6c7075 100%)}

  .gallery{left:402px;top:423px;width:798px;height:426px;overflow:hidden;
    background:linear-gradient(90deg,#3c4044 0%,#9fa3a7 18%,#e9eaeb 40%,#c2c5c8 55%,#f0f1f2 68%,#8d9196 85%,#3f4347 100%)}
  .part{position:absolute;border-radius:10px;box-shadow:3px 5px 8px rgba(0,0,0,.35)}
  .part.grey{background:linear-gradient(135deg,#c4c8cc,#8a8f94)}
  .part.light{background:linear-gradient(135deg,#eef0f1,#b9bdc1)}
  .part.beige{background:linear-gradient(135deg,#e6e3cf,#b9b49a)}
  .part.dark{background:linear-gradient(135deg,#5a5f64,#1e2225)}
  .part.yellow{background:linear-gradient(135deg,#f4cf3a,#c8920e)}
  .part.round{border-radius:50%}
</style>
</head>
<body>

  <header class="abs intro-head">
    <span class="accent-bar" style="left:43px;top:47px;height:28px"></span>
    <h1 class="page-title">What we do?</h1>
  </header>

  <section class="abs intro-panel">
    <p>Vantor Industrial Manufacturing, Inc.<br>We provide contract<br>manufacturing services in<br>precision sheet metal, precision<br>machining, assemblies, and<br>welding. We specialize in fast<br>turnaround support as well as<br>long term production runs. We<br>are a critical part of the supply<br>base for Military, Defense ,<br>Aerospace, High Technology,<br>Electronics and Automotive<br>sectors.</p>
  </section>

  <h2 class="abs sector-head sky" style="left:402px;width:189px">AEROSPACE</h2>
  <h2 class="abs sector-head navy" style="left:600px;width:195px">MILITARY<br>DEFENSE</h2>
  <h2 class="abs sector-head sky" style="left:803px;width:194px;padding-left:18px">HIGH<br>TECHNOLOGY</h2>
  <h2 class="abs sector-head navy" style="left:1005px;width:195px;padding-left:20px">ELECTRONICS<br>&amp; AUTOMOTIVE</h2>

  <p class="abs sector-desc" style="left:402px;width:189px">Build to print sheet metal<br>fabrication, CNC<br>machining &amp; assembly<br>solution for aerospace<br>primes as well as system<br>integrators</p>
  <p class="abs sector-desc" style="left:600px;width:195px;padding-left:22px">Complex fluid systems<br>and assemblies for<br>defense contractors, as<br>well as the US Military</p>
  <p class="abs sector-desc" style="left:803px;width:194px;padding-left:18px">Testing, handling,<br>and enclosures for<br>high tech industries</p>
  <p class="abs sector-desc" style="left:1005px;width:195px;padding-left:20px">Enclosure and<br>machined components<br>for electronics and<br>automotive system<br>providers</p>

  <div class="abs sector-photo" role="img" aria-label="Photo of a rocket launching from its pad amid orange smoke" style="left:402px;width:189px;background:linear-gradient(135deg,#5a1606 0%,#b2380c 40%,#f08a2a 70%,#f4d6a0 100%)"></div>
  <div class="abs sector-photo" role="img" aria-label="Photo of military ground crew working beside a tiltrotor aircraft on a desert airfield" style="left:600px;width:195px;background:linear-gradient(180deg,#5f8fc4 0%,#a9c3de 38%,#b8a98c 60%,#7f7160 100%)"></div>
  <div class="abs sector-photo" role="img" aria-label="Photo of robotic arms on an automated line with a hand holding a tablet" style="left:803px;width:194px;background:linear-gradient(135deg,#1e2c40 0%,#4f6682 45%,#2b5ea8 70%,#1a2333 100%)"></div>
  <div class="abs sector-photo" role="img" aria-label="Photo of a modern dark grey truck cab in a garage" style="left:1005px;width:195px;background:linear-gradient(135deg,#d7dadd 0%,#6e7379 40%,#2a2d31 70%,#9ea2a6 100%)"></div>

  <section class="abs services">
    <span class="accent-bar" style="left:43px;top:36px;height:63px"></span>
    <h2 class="services-title">Our<br>Services</h2>
    <div class="service" style="top:131px;height:41px">Precision Machining</div>
    <div class="service" style="top:191px;height:59px">Precision Sheet Metal<br>Fabrication</div>
    <div class="service" style="top:269px;height:41px">Complex Assemblies</div>
    <div class="service" style="top:328px;height:40px">Complicated Weldments</div>
    <div class="steel-strip"></div>
  </section>

  <section class="abs gallery" aria-label="Showcase of manufactured parts on brushed steel">
    <div class="part grey" style="left:19px;top:39px;width:152px;height:112px" role="img" aria-label="Photo of a grey sheet metal rack frame with copper tubing"></div>
    <div class="part beige" style="left:179px;top:44px;width:150px;height:115px" role="img" aria-label="Photo of beige welded tube frames"></div>
    <div class="part beige" style="left:335px;top:24px;width:128px;height:112px" role="img" aria-label="Photo of an engine-driven fluid system skid"></div>
    <div class="part dark" style="left:479px;top:29px;width:154px;height:102px" role="img" aria-label="Photo of machined dark grey housings"></div>
    <div class="part yellow" style="left:660px;top:21px;width:120px;height:157px" role="img" aria-label="Photo of a yellow test cart with gauges and hose reel"></div>
    <div class="part light" style="left:21px;top:181px;width:128px;height:94px" role="img" aria-label="Photo of a machined triangular ring plate"></div>
    <div class="part light" style="left:168px;top:188px;width:105px;height:125px" role="img" aria-label="Photo of a bracket and ribbed sheet metal panel"></div>
    <div class="part light round" style="left:287px;top:176px;width:40px;height:52px" role="img" aria-label="Photo of a machined aluminium cylinder"></div>
    <div class="part dark round" style="left:367px;top:170px;width:65px;height:70px" role="img" aria-label="Photo of a black anodised cylinder"></div>
    <div class="part grey" style="left:315px;top:241px;width:50px;height:31px" role="img" aria-label="Photo of a small threaded fitting"></div>
    <div class="part light" style="left:476px;top:149px;width:167px;height:107px" role="img" aria-label="Photo of white machined enclosure boxes"></div>
    <div class="part dark" style="left:27px;top:314px;width:141px;height:73px" role="img" aria-label="Photo of a black machined base plate"></div>
    <div class="part beige" style="left:200px;top:330px;width:178px;height:78px" role="img" aria-label="Photo of a painted formed duct"></div>
    <div class="part light" style="left:356px;top:264px;width:146px;height:144px" role="img" aria-label="Photo of machined mounting brackets"></div>
    <div class="part grey" style="left:486px;top:256px;width:183px;height:157px" role="img" aria-label="Photo of a set of machined rail assemblies"></div>
    <div class="part grey round" style="left:627px;top:232px;width:52px;height:50px" role="img" aria-label="Photo of a machined cup"></div>
    <div class="part grey" style="left:675px;top:277px;width:68px;height:57px" role="img" aria-label="Photo of a flanged machined block"></div>
    <div class="part light" style="left:709px;top:250px;width:76px;height:44px" role="img" aria-label="Photo of an angled machined bracket"></div>
  </section>

</body>
</html>
```